Business Cards

We were billed for this because the project timed out. Please give me another designed to open this back up. I was not happy with the last designs (that I was charged for).
we are also using the logo with Caring for Water One Visit at a Time
Also want to utilize Where Healthy Water is our Commitment.

Contact Information for Business Card

Marlowe Stone Group Inc

```html
<!DOCTYPE html>
<html lang="en">
<head>
<meta charset="utf-8">
<title>Marlowe Stone Group – Business Card</title>
<link rel="stylesheet" href="https://fonts.googleapis.com/css2?family=Open+Sans:wght@400;600;700&display=swap">
<style>
  :root {
    --stage: #222222;
    --paper: #ffffff;
    --ink: #1a1a1a;
    --muted: #333333;
    --brand-blue: #136fbf;
    --brand-deep: #0e5fa8;
    --brand-light: #3fa0de;
    --rule: #111111;
    --on-blue: #ffffff;
  }
  * { box-sizing: border-box; margin: 0; padding: 0; }
  html, body { width: 1200px; height: 780px; overflow: hidden; }
  body {
    background: var(--stage);
    font-family: "Open Sans", Arial, sans-serif;
    position: relative;
  }
  .card {
    position: absolute;
    top: 235px;
    width: 540px;
    height: 309px;
    border-radius: 3px;
    overflow: hidden;
    box-shadow: 0 18px 40px rgba(0,0,0,.55);
  }
  .card-front { left: 40px; background: var(--paper); }
  .card-back { left: 620px; }

  /* Front */
  .front-bands { position: absolute; inset: 0; }
  .brand-lockup { position: absolute; left: 30px; top: 30px; }
  .brand-name {
    font-size: 19px; font-weight: 700; letter-spacing: 2px;
    color: var(--brand-blue); text-transform: uppercase;
    display: flex; align-items: center; gap: 8px;
    white-space: nowrap;
  }
  .brand-mark {
    width: 14px; height: 14px; border-radius: 50%;
    background: var(--brand-blue); flex: none;
  }
  .brand-tagline {
    margin-top: 3px; margin-left: 22px;
    font-size: 7.5px; letter-spacing: 1.6px; color: var(--muted);
    text-transform: uppercase; white-space: nowrap;
  }
  .divider {
    position: absolute; left: 34px; top: 145px;
    width: 450px; height: 1.5px; background: var(--rule);
  }
  .holder {
    position: absolute; right: 56px; top: 92px; text-align: right;
  }
  .holder-name {
    font-size: 24px; font-weight: 600; color: var(--brand-blue);
    line-height: 28px; white-space: nowrap;
  }
  .holder-title {
    margin-top: 2px; font-size: 13px; line-height: 18px; color: var(--ink);
    white-space: nowrap;
  }
  .contact-list {
    position: absolute; left: 34px; top: 152px; list-style: none;
    font-size: 11.5px; color: var(--ink); line-height: 18px;
  }
  .contact-list li { display: flex; align-items: center; gap: 7px; white-space: nowrap; }
  .contact-list svg { width: 11px; height: 11px; fill: var(--brand-light); flex: none; }
  .address {
    position: absolute; right: 92px; top: 214px; text-align: right;
    font-size: 13px; line-height: 18px; color: var(--ink); white-space: nowrap;
  }

  /* Back */
  .back-field {
    position: absolute; inset: 0;
    background: linear-gradient(135deg, #1577c9 0%, #136fbf 55%, #0f62ad 100%);
  }
  .back-brand {
    position: absolute; right: 40px; bottom: 40px; text-align: left;
  }
  .back-brand .brand-name { color: var(--on-blue); font-size: 15px; }
  .back-brand .brand-mark { background: var(--on-blue); width: 11px; height: 11px; }
  .back-brand .brand-tagline { color: var(--on-blue); font-size: 6px; margin-left: 19px; }
</style>
</head>
<body>

<section class="card card-front" aria-label="Business card front">
  <svg class="front-bands" viewBox="0 0 540 309" aria-hidden="true">
    <rect x="470" y="170" width="70" height="139" fill="var(--brand-light)"/>
    <path d="M0 262 L300 262 Q310 262 314 272 L318 282 L540 282 L540 309 L0 309 Z" fill="var(--brand-deep)"/>
    <path d="M0 254 L298 254 Q306 254 308 262 L0 262 Z" fill="var(--brand-light)"/>
    <rect x="0" y="249" width="300" height="2" fill="var(--brand-light)"/>
  </svg>

  <div class="brand-lockup">
    <div class="brand-name"><span class="brand-mark"></span>Marlowe Stone Group</div>
    <div class="brand-tagline">Caring for Water One Visit at a Time</div>
  </div>

  <div class="holder">
    <div class="holder-name">Helena Varga</div>
    <div class="holder-title">Managing Director</div>
  </div>

  <div class="divider"></div>

  <ul class="contact-list">
    <li><svg viewBox="0 0 24 24"><path d="M6.6 10.8a15.1 15.1 0 0 0 6.6 6.6l2.2-2.2a1 1 0 0 1 1-.25 11.4 11.4 0 0 0 3.6.57 1 1 0 0 1 1 1V20a1 1 0 0 1-1 1A17 17 0 0 1 3 4a1 1 0 0 1 1-1h3.5a1 1 0 0 1 1 1c0 1.25.2 2.45.57 3.57a1 1 0 0 1-.25 1z"/></svg>(555) 014-2290</li>
    <li><svg viewBox="0 0 24 24"><path d="M2 5h20v14H2z M4 7v.4l8 5 8-5V7l-8 5z" fill-rule="evenodd"/></svg>hello@marlowestone.com</li>
    <li><svg viewBox="0 0 24 24"><circle cx="12" cy="12" r="10"/></svg>www.marlowestone.com</li>
  </ul>

  <div class="address">1840 Cedar Bend Rd. Suite 310<br>Alder Springs, TX 75410</div>
</section>

<section class="card card-back" aria-label="Business card back">
  <div class="back-field" role="img" aria-label="Blue field with a repeating embossed brand pattern"></div>
  <div class="back-brand">
    <div class="brand-name"><span class="brand-mark"></span>Marlowe Stone Group</div>
    <div class="brand-tagline">Caring for Water One Visit at a Time</div>
  </div>
</section>

</body>
</html>
```